Poster design for a vet clinic

Running a campaign called 'Pal Spotter', which is where people get a $30 voucher for themselves and their friend if they refer somebody to our vet clinic.

Text something like:
We love Pal Spotters!
Refer a fur friend to our friendly team and both your fur child and their fur child will receive a $30 voucher to use in clinic! *
* Limited to one pet per fur parent and the referred fur parent must be new to our clinic. Unlimited vouchers for number of referrals!

I want it to be cute but professional. You can see the design styles at vettoly.com.au/northryde and see the logo there too.
I am thinking of having a dog whispering to a cat or something like that as the main image.
I would like both the photoshop file and the pdf please. Would be for an A2 poster.

```html
<!DOCTYPE html>
<html lang="en">
<head>
<meta charset="utf-8">
<title>Pal Spotters – Referral Poster</title>
<link rel="stylesheet" href="https://fonts.googleapis.com/css2?family=Arimo:wght@400;700&family=Gochi+Hand&family=Kaushan+Script&family=Luckiest+Guy&display=swap">
<style>
  :root {
    --paper: #ffffff;
    --bg-top: #5e4538;
    --bg-bottom: #1f1f1f;
    --we-yellow: #f2e21a;
    --heart-red: #e8202e;
    --maroon: #8e1b3a;
    --bubble-yellow: #fdec11;
    --bubble-green: #c0ecb0;
    --accent-pink: #ee1452;
    --ink: #111111;
    --logo-cream: #f9e08f;
    --dog-tone: #e8e8e8;
    --cat-tone: #e8643c;
  }
  html, body {
    margin: 0;
    padding: 0;
    overflow: hidden;
    background: var(--paper);
  }
  .poster {
    position: relative;
    width: 960px;
    height: 1200px;
    background: var(--paper);
    overflow: hidden;
  }
  .poster__field {
    position: absolute;
    left: 18px; top: 18px;
    width: 920px; height: 1160px;
    background: linear-gradient(160deg, var(--bg-top) 0%, #3f3430 50%, var(--bg-bottom) 100%);
  }
  .headline-we {
    position: absolute;
    left: 52px; top: 46px;
    width: 120px;
    margin: 0;
    font-family: "Gochi Hand", cursive;
    font-weight: 400;
    font-size: 104px;
    line-height: 110px;
    text-align: center;
    color: var(--we-yellow);
    transform: rotate(-50deg);
    transform-origin: 50% 50%;
  }
  .heart {
    position: absolute;
    left: 152px; top: 142px;
    width: 58px; height: 56px;
    transform: rotate(-20deg);
  }
  .art {
    position: absolute;
  }
  .art--dog {
    left: 240px; top: 48px;
    width: 320px; height: 228px;
    background: linear-gradient(135deg, #1a1a1a 0%, var(--dog-tone) 45%, #ffffff 100%);
    border-radius: 45% 40% 30% 35%;
  }
  .art--cat {
    left: 64px; top: 232px;
    width: 240px; height: 232px;
    border-radius: 40% 50% 45% 50%;
    background: radial-gradient(circle at 50% 45%, #f27a52 0%, var(--cat-tone) 70%);
  }
  .title-band {
    position: absolute;
    left: 0; top: 271px;
    width: 800px; height: 130px;
    background: var(--paper);
    border-radius: 65px;
    transform: rotate(-35deg);
    box-shadow: 14px 14px 18px rgba(0,0,0,0.45);
    display: flex;
    align-items: center;
    justify-content: center;
  }
  .title-band__text {
    margin: 0;
    font-family: "Gochi Hand", cursive;
    font-weight: 400;
    font-size: 100px;
    line-height: 1;
    color: var(--maroon);
    letter-spacing: 2px;
    white-space: nowrap;
  }
  .bubbles {
    position: absolute;
    left: 0; top: 0;
    width: 960px; height: 1200px;
  }
  .bubble-text {
    position: absolute;
    margin: 0;
    font-family: "Kaushan Script", cursive;
    color: var(--ink);
    text-align: center;
    white-space: nowrap;
  }
  .bubble-text em {
    font-style: normal;
    font-family: "Luckiest Guy", "Arial Black", sans-serif;
    color: var(--accent-pink);
    letter-spacing: 1px;
  }
  .bubble-text--terms {
    left: 470px; top: 520px;
    width: 400px;
    font-size: 22px;
    line-height: 52px;
    transform: rotate(21deg);
  }
  .bubble-text--offer {
    left: 250px; top: 680px;
    width: 460px;
    font-size: 23px;
    line-height: 50px;
    transform: rotate(8deg);
  }
  .clinic-name {
    position: absolute;
    left: 70px; top: 1040px;
    display: flex;
    align-items: center;
    gap: 14px;
    margin: 0;
    font-family: "Arimo", sans-serif;
    font-weight: 700;
    font-size: 40px;
    line-height: 1;
    color: var(--logo-cream);
  }
  .clinic-name__mark {
    width: 32px; height: 32px;
    background: var(--logo-cream);
  }
  .unlimited {
    position: absolute;
    left: 552px; top: 952px;
    width: 360px;
    margin: 0;
    font-family: "Arimo", sans-serif;
    font-weight: 700;
    text-align: center;
  }
  .unlimited__lead {
    display: block;
    font-size: 46px;
    line-height: 56px;
    color: var(--accent-pink);
    letter-spacing: 1px;
  }
  .unlimited__rest {
    display: block;
    margin-top: 32px;
    font-size: 27px;
    line-height: 82px;
    color: var(--paper);
  }
</style>
</head>
<body>
<main class="poster">
  <div class="poster__field"></div>

  <div class="art art--dog" role="img" aria-label="Cartoon black and white dog leaning over the bone to whisper"></div>
  <div class="art art--cat" role="img" aria-label="Cartoon orange cat with big purple eyes looking surprised"></div>

  <h1 class="headline-we">WE</h1>
  <svg class="heart" viewBox="0 0 62 60" aria-label="love" role="img">
    <path d="M31 58 C10 42 0 30 0 17 C0 7 8 0 17 0 C24 0 29 4 31 10 C33 4 38 0 45 0 C54 0 62 7 62 17 C62 30 52 42 31 58 Z" fill="var(--heart-red)"/>
  </svg>

  <div class="title-band">
    <h2 class="title-band__text">PAL SPOTTERS</h2>
  </div>

  <svg class="bubbles" viewBox="0 0 960 1200" aria-hidden="true">
    <defs>
      <filter id="bubble-shadow" x="-20%" y="-20%" width="140%" height="140%">
        <feDropShadow dx="10" dy="10" stdDeviation="8" flood-color="#000" flood-opacity="0.45"/>
      </filter>
    </defs>
    <path class="bubble bubble--terms" filter="url(#bubble-shadow)" fill="var(--bubble-yellow)"
      d="M760 478 C800 440 820 430 842 418 C815 450 800 480 795 500 C880 560 930 640 900 710 C860 790 720 800 600 770 C480 740 420 660 440 580 C470 480 620 440 760 478 Z"/>
    <path class="bubble bubble--offer" filter="url(#bubble-shadow)" fill="var(--bubble-green)"
      d="M400 936 C300 900 210 840 218 770 C228 680 370 630 510 640 C660 650 760 720 740 810 C722 890 600 935 470 935 C430 970 390 985 352 998 C380 975 395 955 400 936 Z"/>
  </svg>

  <p class="bubble-text bubble-text--terms">
    Limited to <em>ONE PET PER FUR</em><br>
    <em>PARENT</em> and the referred fur<br>
    parent must be <em>NEW</em> to our clinic.
  </p>

  <p class="bubble-text bubble-text--offer">
    Refer a fur friend to our friendly<br>
    team and both your fur child and<br>
    their fur child will receive a <em>$30</em><br>
    voucher to use in clinic!
  </p>

  <p class="clinic-name"><span class="clinic-name__mark"></span>Pawford Vets</p>

  <p class="unlimited">
    <span class="unlimited__lead">UNLIMITED</span>
    <span class="unlimited__rest">vouchers for number of<br>referrals!</span>
  </p>
</main>
</body>
</html>
```